Corvale Real Estate

I manage 2 firms. The first one is Pelmora and the logo is in blue (see the file) but i need a design for my business card for the second firm called CORVALE IMMOBILIER. This one is in charge of Real estate developer.

Colors
3176b5

```html
<!DOCTYPE html>
<html lang="en">
<head>
<meta charset="utf-8">
<title>Corvale Immobilier – Business Card</title>
<link rel="stylesheet" href="https://fonts.googleapis.com/css2?family=Montserrat:wght@600&family=Arimo:wght@400;700&display=swap">
<style>
  :root {
    --brand-blue: #3260ae;
    --card-white: #ffffff;
    --ink-grey: #6f7378;
    --stage: #2b2c30;
  }
  * { margin: 0; padding: 0; box-sizing: border-box; }
  html, body { width: 1200px; height: 800px; overflow: hidden; }
  body { background: var(--stage); position: relative; }

  .card {
    position: absolute;
    width: 560px;
    height: 320px;
    border-radius: 22px;
    box-shadow: 0 14px 30px rgba(0,0,0,.35);
  }

  /* Front */
  .card--front {
    left: 150px; top: 60px;
    background: var(--brand-blue);
    display: flex; align-items: center; justify-content: center;
  }
  .brand { display: flex; align-items: center; gap: 22px; }
  .brand__square { width: 46px; height: 46px; background: var(--card-white); }
  .brand__name {
    font-family: "Montserrat", sans-serif; font-weight: 600;
    color: var(--card-white); line-height: 1;
  }
  .brand__main { font-size: 44px; letter-spacing: 9px; display: block; }
  .brand__sub { font-size: 15px; letter-spacing: 10px; display: block; margin-top: 10px; }

  /* Back */
  .card--back {
    left: 490px; top: 420px;
    background: var(--card-white);
    padding: 44px 48px;
  }
  .back-brand {
    font-family: "Montserrat", sans-serif; font-weight: 600;
    color: var(--brand-blue); line-height: 1;
  }
  .back-brand__main { font-size: 40px; letter-spacing: 8px; display: block; }
  .back-brand__sub { font-size: 14px; letter-spacing: 9px; display: block; margin-top: 8px; }

  .person { margin-top: 26px; font-family: "Arimo", sans-serif; }
  .person__name { color: var(--brand-blue); font-weight: 700; font-size: 17px; }
  .person__role { color: var(--ink-grey); font-size: 14px; margin-top: 2px; }

  .contact { margin-top: 14px; font-family: "Arimo", sans-serif; font-size: 14px; color: var(--ink-grey); list-style: none; }
  .contact li { display: flex; align-items: center; gap: 9px; line-height: 1.45; }
  .contact .no-icon { padding-left: 23px; }
  .contact svg { width: 14px; height: 14px; flex: none; }
  .contact .web { color: var(--brand-blue); }
</style>
</head>
<body>

<section class="card card--front" aria-label="Card front">
  <div class="brand">
    <span class="brand__square"></span>
    <span class="brand__name">
      <span class="brand__main">CORVALE</span>
      <span class="brand__sub">IMMOBILIER</span>
    </span>
  </div>
</section>

<section class="card card--back" aria-label="Card back">
  <div class="back-brand">
    <span class="back-brand__main">CORVALE</span>
    <span class="back-brand__sub">IMMOBILIER</span>
  </div>

  <div class="person">
    <p class="person__name">LENA MARDIS</p>
    <p class="person__role">Manager</p>
  </div>

  <ul class="contact">
    <li class="no-icon">PO BOX 48, Harrow Street</li>
    <li class="no-icon">3rd Lane, Ferndale 60418</li>
    <li>
      <svg viewBox="0 0 14 14" aria-hidden="true"><rect x="3" y="1" width="8" height="12" rx="1.5" fill="none" stroke="#3260ae" stroke-width="1.6"/></svg>
      (555) 204 3187
    </li>
    <li>
      <svg viewBox="0 0 14 14" aria-hidden="true"><rect x="1" y="3" width="12" height="8" fill="#3260ae"/><path d="M1 3l6 4.5L13 3" fill="none" stroke="#fff" stroke-width="1.2"/></svg>
      info@corvalemail.com
    </li>
    <li>
      <svg viewBox="0 0 14 14" aria-hidden="true"><circle cx="7" cy="7" r="6" fill="#3260ae"/><path d="M1 7h12M7 1c-3 3-3 9 0 12M7 1c3 3 3 9 0 12" fill="none" stroke="#fff" stroke-width="0.9"/></svg>
      <span>www.<span class="web">corvaleweb</span>.com</span>
    </li>
  </ul>
</section>

</body>
</html>
```